GPS Tracker Business Card Design

We need a business card for a GPS Vehicle tracking company. We sell the hardware for the vehicle and the software platform to monitor your vehicle/s. Including high asset non-powered vehicles like a trailer using our solar powered unit.
We like using dark blue to different shades of blue along with gold. We have phone apps for Android and Apple devices.

We have a platform for families wanting to track their teenage driver and children; Plus a Fleet vehicle tracking platform.

Features: unlimited number of vehicles and/or assets including snow mobiles forklifts generators trailers airport equipment

Reports for driving behavior reports and alerts dashboard fleet maintenace timeline view and replay geofence real time alerts logbook scheduling route optimization accounting integration fleet grouping closest vehicle locator On Board Diagnostics.

Benefits: Increased productivity improved fuel efficiency organizing your business improve time management simplify back end processes, reduce fleet fuel efficiency and expenses increase fleet security etc..

Please view website: Velmorix.com

Industry/Entity Type

Business

Contact Information for Business Card

Harold P Simkins

```html
<!DOCTYPE html>
<html lang="en">
<head>
<meta charset="utf-8">
<title>Velmorix Business Card</title>
<link href="https://fonts.googleapis.com/css2?family=Barlow:wght@300;400;500;700&display=swap" rel="stylesheet">
<style>
  :root {
    --page: #2a2827;
    --card: #131313;
    --white: #f4f4f4;
    --grey: #6c6c6c;
    --gold: #f0b13c;
    --blue: #1d5db5;
    --globe-top: #26344d;
    --globe-bottom: #18202f;
    --dots: #2f86c4;
  }
  * { margin: 0; padding: 0; box-sizing: border-box; }
  html, body { width: 1200px; height: 1200px; overflow: hidden; }
  body {
    background: var(--page);
    font-family: "Barlow", Arial, sans-serif;
    position: relative;
  }
  .card {
    position: absolute;
    left: 250px;
    width: 700px;
    height: 400px;
    background: var(--card);
    overflow: hidden;
    box-shadow: 0 10px 30px rgba(0,0,0,.5);
  }
  .card--promo { top: 140px; text-align: center; }
  .card--contact { top: 620px; }

  .brand-name {
    font-weight: 300;
    color: var(--white);
    letter-spacing: -1px;
    line-height: 1;
  }
  .tagline {
    color: var(--grey);
    font-weight: 400;
    white-space: nowrap;
  }

  /* promo side */
  .card--promo .brand-name { font-size: 96px; margin-top: 78px; }
  .card--promo .tagline { font-size: 26px; margin-top: 4px; }
  .promo-phone {
    color: var(--gold);
    font-weight: 700;
    font-size: 36px;
    margin-top: 34px;
    letter-spacing: 1px;
  }
  .promo-call {
    color: var(--white);
    font-size: 24px;
    margin-top: 4px;
  }
  .promo-call strong { font-weight: 700; }
  .promo-footer {
    position: absolute;
    left: 0; right: 0; bottom: 28px;
    font-size: 17px;
    color: var(--gold);
  }
  .promo-footer .site { color: var(--white); }

  /* contact side */
  .card--contact .brand { position: absolute; left: 120px; top: 30px; }
  .card--contact .brand-name { font-size: 84px; }
  .card--contact .tagline { font-size: 22px; margin-top: 2px; }
  .satellite { position: absolute; left: 105px; top: 178px; }
  .name-plate {
    position: absolute;
    left: 400px; top: 180px;
    width: 225px;
    background: var(--gold);
    border-radius: 4px;
    padding: 10px 12px 12px;
    text-align: center;
  }
  .name-plate .person { color: var(--blue); font-weight: 500; font-size: 27px; line-height: 1.1; white-space: nowrap; }
  .name-plate .role { color: #1a1a1a; font-size: 17px; margin-top: 2px; }
  .name-plate .cell { color: #1a1a1a; font-size: 17px; }
  .globe { position: absolute; left: 0; top: 0; }
  .slogan {
    position: absolute;
    left: 0; right: 0; bottom: 40px;
    text-align: center;
    color: var(--blue);
    font-size: 19px;
    letter-spacing: 1px;
  }
</style>
</head>
<body>

<section class="card card--promo">
  <div class="brand-name">Velmorix</div>
  <div class="tagline">Every Road, Always In View</div>
  <div class="promo-phone">800-555-0147</div>
  <div class="promo-call">Call today for a <strong>Free demo</strong></div>
  <div class="promo-footer">GPS Tracking System - <span class="site">Velmorix.com</span></div>
</section>

<section class="card card--contact">
  <svg class="globe" width="700" height="400" viewBox="0 0 700 400">
    <defs>
      <linearGradient id="globeFill" x1="0" y1="0" x2="0" y2="1">
        <stop offset="0" stop-color="var(--globe-top)"/>
        <stop offset="1" stop-color="var(--globe-bottom)"/>
      </linearGradient>
      <linearGradient id="mapFill" x1="0" y1="0" x2="0" y2="1">
        <stop offset="0" stop-color="var(--dots)" stop-opacity=".45"/>
        <stop offset="1" stop-color="var(--dots)" stop-opacity=".1"/>
      </linearGradient>
    </defs>
    <path d="M0 265 Q330 215 700 300 L700 345 Q360 330 0 355 Z" fill="url(#globeFill)"/>
    <path role="img" aria-label="Dotted world map along the curve of the earth"
          d="M0 265 Q330 215 700 300 L700 345 Q360 330 0 355 Z" fill="url(#mapFill)"/>
    <g class="pin" transform="translate(330 248)">
      <path d="M0 -36 C-13 -36 -20 -27 -20 -18 C-20 -5 0 14 0 14 C0 14 20 -5 20 -18 C20 -27 13 -36 0 -36 Z" fill="var(--gold)"/>
      <circle cx="0" cy="-18" r="7" fill="var(--card)"/>
    </g>
  </svg>

  <div class="brand">
    <div class="brand-name">Velmorix</div>
    <div class="tagline">Every Road, Always In View</div>
  </div>

  <svg class="satellite" width="90" height="60" viewBox="0 0 90 60" role="img" aria-label="Satellite icon">
    <g transform="rotate(-20 45 30)">
      <rect x="2" y="20" width="30" height="16" fill="#555"/>
      <rect x="38" y="16" width="14" height="24" fill="#666"/>
      <rect x="58" y="20" width="30" height="16" fill="#555"/>
      <line x1="32" y1="28" x2="58" y2="28" stroke="#666" stroke-width="2"/>
    </g>
  </svg>

  <div class="name-plate">
    <div class="person">Harold P Simkins</div>
    <div class="role">CEO</div>
    <div class="cell">Cell: 555 210 7389</div>
  </div>

  <div class="slogan">Smarter Fleets, Safer Journeys</div>
</section>

</body>
</html>
```